New Business Card Design Project

I need a meaningful new business card. Therefore, the website should convey growth, joy, uniqueness, workout and a bit of luxury.
Color scheme should be petrol, gold and matching colors.

```html
<!DOCTYPE html>
<html lang="en">
<head>
<meta charset="utf-8">
<title>Core Studio Alpen – Business Card</title>
<link rel="stylesheet" href="https://fonts.googleapis.com/css2?family=EB+Garamond:wght@400;500&family=Great+Vibes&display=swap">
<style>
  :root {
    --stage: #e4e4e2;
    --ink: #1e1a1b;
    --card-dark: #221e1f;
    --card-light: #ffffff;
    --card-light-shade: #ececec;
    --petrol: #1aa89a;
    --gold: #c8942c;
    --text: #3a3a3a;
  }
  * { margin: 0; padding: 0; box-sizing: border-box; }
  html, body { width: 1200px; height: 900px; overflow: hidden; }
  body {
    background: var(--stage);
    font-family: "EB Garamond", Georgia, serif;
    color: var(--text);
    position: relative;
  }
  .card {
    position: absolute;
    width: 620px;
    height: 354px;
    left: 290px;
    border-radius: 4px;
    overflow: hidden;
    box-shadow: 0 10px 28px rgba(0,0,0,.25);
  }
  .card--back { top: 60px; background: var(--card-dark); }
  .card--front {
    top: 480px;
    background: linear-gradient(100deg, var(--card-light-shade) 0%, var(--card-light) 55%, var(--card-light) 100%);
  }

  .brand {
    position: absolute;
    display: flex;
    align-items: center;
    gap: 10px;
    font-family: "EB Garamond", Georgia, serif;
    font-weight: 500;
    white-space: nowrap;
  }
  .brand__dot { width: 14px; height: 14px; border-radius: 50%; background: currentColor; }
  .card--back .brand { color: var(--gold); font-size: 34px; left: 50%; top: 50%; transform: translate(-50%, -50%); }
  .card--front .brand { color: var(--petrol); font-size: 24px; right: 40px; top: 62px; }

  .person { position: absolute; left: 70px; top: 96px; }
  .person__name {
    font-family: "Great Vibes", cursive;
    color: var(--petrol);
    font-size: 38px;
    line-height: 1;
  }
  .person__role { font-size: 15px; line-height: 1.25; margin-top: 2px; }
  .person__address { font-size: 15px; line-height: 1.25; margin: 12px 0 0 34px; }

  .contact { list-style: none; margin: 12px 0 0 56px; font-size: 15px; line-height: 1.4; }
  .contact li { display: flex; align-items: center; gap: 10px; white-space: nowrap; }
  .contact svg { width: 14px; height: 14px; flex: none; fill: none; stroke: var(--petrol); stroke-width: 2; }

  .band--dark {
    position: absolute; left: 0; bottom: 0;
    width: 350px; height: 34px;
    background: var(--ink);
  }
  .band--petrol {
    position: absolute; right: 0; bottom: 0;
    width: 270px; height: 120px;
    background: var(--petrol);
    border-top-left-radius: 26px;
    display: flex; align-items: center; justify-content: center; gap: 8px;
    color: var(--ink); font-size: 15px;
  }
  .band__icon { width: 12px; height: 12px; border-radius: 50%; background: var(--ink); }
</style>
</head>
<body>
  <section class="card card--back" aria-label="Card back">
    <div class="brand"><span class="brand__dot"></span>Core Studio Alpen</div>
  </section>

  <section class="card card--front" aria-label="Card front">
    <div class="brand"><span class="brand__dot"></span>Core Studio Alpen</div>

    <div class="person">
      <div class="person__name">Lena Maurer</div>
      <div class="person__role">Pilates Trainer</div>
      <div class="person__address">Lindenweg 12<br>83000 Talheim</div>
      <ul class="contact">
        <li><svg viewBox="0 0 16 16"><path d="M3 2l3 1 1 3-2 1a8 8 0 0 0 4 4l1-2 3 1 1 3-2 1C7 14 2 9 2 4z"/></svg>+49 170 5550192</li>
        <li><svg viewBox="0 0 16 16"><rect x="1.5" y="3.5" width="13" height="9"/><path d="M1.5 3.5l6.5 5 6.5-5"/></svg>hello@corestudio-alpen.de</li>
        <li><svg viewBox="0 0 16 16"><circle cx="8" cy="8" r="6.5"/><path d="M1.5 8h13M8 1.5c-3 3.5-3 9.5 0 13M8 1.5c3 3.5 3 9.5 0 13"/></svg>corestudio-alpen.de</li>
      </ul>
    </div>

    <div class="band--dark"></div>
    <div class="band--petrol">corestudio_alpen<span class="band__icon"></span></div>
  </section>
</body>
</html>
```